Small business updating business cards

We have already updated our logo via Pixel Forum and downloaded it (hopefully) for you to use. Now an updated set of business cards for Neil Pollard and Stuart Pollard are also needed... we are also hoping that a copy of our outdated business card designs have uploaded successfully as Microsoft Publisher files. Our Strength Through Unity motto has died a slow death so we are hoping to remove it (and other superfluous lingo if the graphic covers the idea) and instead opt for a fancy graphic (?) on the second side of the card that really reflects our desire to obtain product / haulage from Road Transport / Yard Operators and convert legs of their haulage to rail freight where profitable (bulk haulage / containterised etc). Can you help us look larger, bolder and more robust than we really are (two man show)?
Target Market(s)
Transport Industry
Industry/Entity Type
Business
Contact Information for Business Card
Card details for both N Pollard and S Pollard have been uploaded on the publisher files
Colors
Designer to choose colors to be used in the design.
Requirements
Must have
- Similar theme both sides of card
Should not have
- Black on one side white on the other

```html
<!DOCTYPE html>
<html lang="en">
<head>
<meta charset="utf-8">
<title>Raylink Haul — Business Card</title>
<link href="https://fonts.googleapis.com/css2?family=Open+Sans:wght@400;600;700&display=swap" rel="stylesheet">
<style>
  :root {
    --backdrop: #3a3a3a;
    --card-white: #ffffff;
    --teal: #3f8a8a;
    --gold: #d69c0f;
    --ink: #505050;
    --divider: #9a9a9a;
    --back-top: #23869e;
    --back-bottom: #9a9132;
  }
  * { margin: 0; padding: 0; box-sizing: border-box; }
  html, body {
    width: 1200px; height: 960px; overflow: hidden;
    background: var(--backdrop);
    font-family: "Open Sans", Arial, sans-serif;
  }
  .card {
    position: absolute;
    width: 600px; height: 342px;
    border-radius: 22px;
    overflow: hidden;
  }
  .card--front { left: 302px; top: 136px; background: var(--card-white); }
  .card--back {
    left: 299px; top: 495px;
    background: linear-gradient(to bottom, var(--back-top), var(--back-bottom));
  }
  .brand-name {
    position: absolute;
    font-weight: 700;
    white-space: nowrap;
    letter-spacing: -0.5px;
  }
  .card--front .brand-name {
    left: 50px; top: 152px;
    font-size: 35px; line-height: 44px; color: var(--teal);
  }
  .card--back .brand-name {
    left: 0; right: 0; top: 134px; text-align: center;
    font-size: 56px; line-height: 72px; color: #ffffff;
  }
  .divider {
    position: absolute; left: 312px; top: 62px;
    width: 2px; height: 232px;
    background: linear-gradient(to bottom, transparent, var(--divider) 20%, var(--divider) 80%, transparent);
  }
  .details { position: absolute; left: 343px; top: 63px; color: var(--ink); }
  .person-name { font-size: 20px; font-weight: 600; color: var(--teal); line-height: 28px; }
  .person-role { font-size: 16px; color: var(--gold); line-height: 22px; }
  .address { margin-top: 10px; font-size: 16px; line-height: 22px; }
  .contact-list { list-style: none; margin-top: 6px; }
  .contact-list li {
    display: flex; align-items: center;
    font-size: 16px; line-height: 22.8px; white-space: nowrap;
  }
  .contact-list svg { width: 17px; height: 17px; margin-right: 7px; fill: var(--teal); flex: none; }
</style>
</head>
<body>
  <section class="card card--front">
    <div class="brand-name">Raylink Haul</div>
    <div class="divider"></div>
    <div class="details">
      <div class="person-name">NEIL POLLARD</div>
      <div class="person-role">CEO/Founder</div>
      <div class="address">214 Siding Road<br>Junction Falls, Ohio 41208</div>
      <ul class="contact-list">
        <li><svg viewBox="0 0 16 16"><path d="M3 1l3 3-1.5 2a9 9 0 0 0 5.5 5.5L12 10l3 3-2 2C7 15 1 9 1 3z"/></svg>555 210 4471</li>
        <li><svg viewBox="0 0 16 16"><path d="M4 0h8a1 1 0 0 1 1 1v14a1 1 0 0 1-1 1H4a1 1 0 0 1-1-1V1a1 1 0 0 1 1-1zm1 2v10h6V2zm3 11a1 1 0 1 0 0 2 1 1 0 0 0 0-2z"/></svg>555 318 2096</li>
        <li><svg viewBox="0 0 16 16"><path d="M4 1h8v4H4zM1 6h14v7h-3v2H4v-2H1zm4 5v3h6v-3z"/></svg>555 640 7753</li>
        <li><svg viewBox="0 0 16 16"><path d="M1 3h14v10H1zm1 1.5V5l6 4 6-4v-.5z"/></svg>name@raylinkhaul.com</li>
        <li><svg viewBox="0 0 16 16"><circle cx="8" cy="8" r="7"/><path d="M4 5l3 1 1 3-2 2 1 3M10 3l1 3 3 1" stroke="#fff" stroke-width="1.2" fill="none"/></svg>www.raylinkhaul.com</li>
      </ul>
    </div>
  </section>

  <section class="card card--back">
    <div class="brand-name">Raylink Haul</div>
  </section>
</body>
</html>
```